Concise,Good colour matching,Good looks design for "HERD SURE RAPID TEST FOR LIVESTOCK"

Product Positioning: Affordable test for Large Animals (Livestock/Veterinary Use)
Product Name: HERD SURE Rapid Test Kit (for large animals, e.g., cattle, horses, swine,Avian,sheep).

2. Packaging Requirements

A. Visual Design
Color Scheme:
Green/Blue/Orange/Yellow/Red/Gray/White(chose 2~4 colors)

Mandatory Info:
Brand logo ("HERD SURE")

Target Market(s)

Southeast Asia, Africa, Middle East, South America

Industry/Entity Type

Veterinary diagnostic for LIVESTOCK

Colors

Designer to choose colors to be used in the design.

Requirements
Nice to have
• Concise,Good colour matching,Good looks

```html
<!DOCTYPE html>
<html lang="en">
<head>
<meta charset="utf-8">
<title>HERD SURE Rapid Test for Livestock – Carton Dieline</title>
<link href="https://fonts.googleapis.com/css2?family=Montserrat:wght@500;600;700;800&family=Open+Sans:wght@400;600&display=swap" rel="stylesheet">
<style>
  :root{
    --brand-blue:#2b7cc8;
    --brand-slate:#667585;
    --brand-grey:#8e969c;
    --band-grey:#6f7a86;
    --ink:#4a5560;
    --cut-line:#e0399a;
    --paper:#ffffff;
    --animal-deep:#1f3f78;
    --animal-light:#7fb0e3;
  }
  *{box-sizing:border-box;margin:0;padding:0}
  html,body{width:1200px;height:890px;overflow:hidden;background:var(--paper)}
  body{position:relative;font-family:"Open Sans",Arial,sans-serif;color:var(--ink)}

  .dieline{position:absolute;left:0;top:0;width:1200px;height:890px}
  .brand-name{font-family:"Montserrat",Arial,sans-serif;font-weight:800;color:var(--brand-blue);letter-spacing:.5px;line-height:1;white-space:nowrap}
  .tagline{font-family:"Montserrat",Arial,sans-serif;font-weight:500;color:var(--brand-slate);letter-spacing:1.2px;white-space:nowrap}

  .panel{position:absolute}
  .upside-down{transform:rotate(180deg)}

  /* top tuck flap */
  .panel--top{left:275px;top:48px;width:310px;height:165px;text-align:center}
  .panel--top .brand-name{font-size:28px;margin-top:68px}
  .panel--top .tagline{font-size:8.6px;margin-top:8px}

  /* back panel */
  .panel--back{left:275px;top:420px;width:310px;height:165px;text-align:center}
  .panel--back .brand-name{font-size:28px;margin-top:54px}
  .panel--back .tagline{font-size:8.6px;margin-top:8px}

  /* left side panel: features */
  .panel--features{left:68px;top:420px;width:207px;height:165px;padding:16px 0 0 24px}
  .panel--features .brand-name{font-size:16px;margin-bottom:8px}
  .feature{margin-bottom:7px}
  .feature-title{font-family:"Montserrat",Arial,sans-serif;font-weight:700;font-size:6.8px;color:var(--brand-blue);letter-spacing:.4px;display:flex;align-items:center;gap:3px}
  .feature-title svg{width:7px;height:7px}
  .feature-text{font-size:6px;line-height:1.35;color:var(--ink)}

  /* right side panel: info */
  .panel--info{left:585px;top:420px;width:207px;height:165px;padding:62px 0 0 48px}
  .panel--info .brand-name{font-size:16px}
  .panel--info .product-line{font-family:"Montserrat",Arial,sans-serif;font-weight:500;font-size:7.6px;letter-spacing:.8px;color:var(--brand-slate);margin-top:5px;white-space:nowrap}
  .storage-info{position:absolute;left:16px;top:128px;font-size:6px;line-height:1.35;color:var(--ink)}

  /* front panel */
  .panel--front{left:275px;top:585px;width:310px;height:207px;overflow:hidden}
  .panel--front .brand-name{position:absolute;left:20px;top:34px;font-size:22px}
  .panel--front .tagline{position:absolute;left:20px;top:60px;font-size:7px;line-height:1.4;letter-spacing:.6px}
  .timer{position:absolute;left:227px;top:20px;width:80px;height:56px}
  .band-blue{position:absolute;left:0;top:93px;width:310px;height:60px;background:var(--brand-blue)}
  .band-grey{position:absolute;left:0;top:153px;width:310px;height:18px;background:var(--band-grey)}
  .product-title{position:absolute;left:20px;top:108px;font-family:"Montserrat",Arial,sans-serif;font-weight:700;font-size:12.5px;line-height:1.2;color:#fff}
  .range-label{position:absolute;left:21px;top:156px;font-family:"Montserrat",Arial,sans-serif;font-weight:700;font-size:8.6px;letter-spacing:2.2px;color:#fff}
  .pack-count{position:absolute;left:20px;top:181px;font-family:"Montserrat",Arial,sans-serif;font-weight:500;font-size:7.6px;letter-spacing:.4px;color:var(--brand-slate)}
  .herd-artwork{position:absolute;left:126px;top:68px;width:184px;height:126px;border-radius:40% 40% 6px 6px / 30% 30% 6px 6px;background:radial-gradient(ellipse at 55% 45%,var(--animal-light),var(--animal-deep) 75%)}

  /* large brand lockup */
  .lockup{position:absolute;left:658px;top:712px;width:454px;text-align:center}
  .lockup .brand-name{font-size:72px;letter-spacing:1px}
  .lockup .lockup-line{font-family:"Montserrat",Arial,sans-serif;font-weight:600;font-size:22px;letter-spacing:3.4px;color:var(--brand-grey);margin-top:14px;white-space:nowrap}
</style>
</head>
<body>

<svg class="dieline" viewBox="0 0 1200 890" aria-hidden="true">
  <!-- blue inner panel with side tabs -->
  <path d="M275 213 H585 L622 219 Q631 222 631 232 V402 Q631 412 622 415 L585 420 H275 L238 415 Q228 412 228 402 V232 Q228 222 238 219 Z" fill="#2b7cc8" stroke="#e0399a" stroke-width="0.8"/>
  <g fill="none" stroke="#e0399a" stroke-width="0.8">
    <!-- top flap -->
    <rect x="275" y="48" width="310" height="165"/>
    <!-- middle row -->
    <rect x="68" y="420" width="207" height="165"/>
    <rect x="275" y="420" width="310" height="165"/>
    <rect x="585" y="420" width="207" height="165"/>
    <!-- glue tabs -->
    <path d="M68 420 L33 425 Q21 428 21 440 V565 Q21 577 33 580 L68 585"/>
    <path d="M792 420 L827 425 Q838 428 838 440 V565 Q838 577 827 580 L792 585"/>
    <!-- dust flaps -->
    <path d="M68 585 L73 670 Q74 684 88 684 H255 Q268 684 269 670 L275 585"/>
    <path d="M585 585 L590 670 Q591 684 604 684 H772 Q785 684 786 670 L792 585"/>
    <!-- front panel -->
    <rect x="275" y="585" width="310" height="207"/>
    <!-- bottom tuck -->
    <path d="M275 792 L280 828 Q282 838 292 838 H568 Q578 838 580 828 L585 792"/>
  </g>
</svg>

<section class="panel panel--top">
  <div class="brand-name">HERD SURE</div>
  <div class="tagline">AFFORDABLE DIAGNOSTICS FOR HEALTHY HERDS</div>
</section>

<section class="panel panel--back upside-down">
  <div class="brand-name">HERD SURE</div>
  <div class="tagline">AFFORDABLE DIAGNOSTICS FOR HEALTHY HERDS</div>
</section>

<section class="panel panel--features upside-down">
  <div class="brand-name">HERD SURE</div>
  <div class="feature">
    <div class="feature-title"><svg viewBox="0 0 10 10"><path d="M1 9 L9 1" stroke="#2b7cc8" stroke-width="2"/></svg>FAST &amp; EFFICIENT</div>
    <div class="feature-text">Rapid test results in less than 10 minutes<br>from prep to completion</div>
  </div>
  <div class="feature">
    <div class="feature-title"><svg viewBox="0 0 10 10"><path d="M1 9 L9 1" stroke="#2b7cc8" stroke-width="2"/></svg>AFFORDABLE</div>
    <div class="feature-text">Colloidal gold-based rapid tests that combine<br>high accuracy with cost-effectiveness.</div>
  </div>
  <div class="feature">
    <div class="feature-title"><svg viewBox="0 0 10 10"><path d="M1 9 L9 1" stroke="#2b7cc8" stroke-width="2"/></svg>RELIABLE &amp; SIMPLE</div>
    <div class="feature-text">Stable test performance with 2-30°C. Easy to<br>operate, no professional skills required.</div>
  </div>
</section>

<section class="panel panel--info upside-down">
  <div class="brand-name">HERD SURE</div>
  <div class="product-line">RAPID TEST FOR LIVESTOCK</div>
  <div class="storage-info">Manufactured by AGROVIA<br>Storage: 2-30°C. Do not freeze<br>See the instructions for other contents</div>
</section>

<section class="panel panel--front">
  <div class="brand-name">HERD SURE</div>
  <div class="tagline">AFFORDABLE DIAGNOSTICS<br>FOR HEALTHY HERDS</div>
  <svg class="timer" viewBox="0 0 80 56" aria-label="Results in 10 minutes">
    <defs><path id="timer-arc" d="M8 30 A22 22 0 0 1 52 30"/></defs>
    <text font-family="Montserrat, sans-serif" font-size="6" font-weight="600" letter-spacing="1" fill="#4a5560"><textPath href="#timer-arc" startOffset="12%">RESULTS IN</textPath></text>
    <circle cx="30" cy="32" r="18" fill="none" stroke="#4a5560" stroke-width="0.8" stroke-dasharray="100 14"/>
    <text x="15" y="40" font-family="Montserrat, sans-serif" font-size="21" font-weight="600" fill="#2b7cc8">10</text>
    <text x="41" y="40" font-family="Montserrat, sans-serif" font-size="12" font-weight="600" fill="#2b7cc8">min</text>
  </svg>
  <div class="band-blue"></div>
  <div class="band-grey"></div>
  <div class="product-title">RAPID TEST<br>FOR LIVESTOCK</div>
  <div class="range-label">LARGE ANIMALS</div>
  <div class="pack-count">10 KITS / BOX</div>
  <div class="herd-artwork" role="img" aria-label="Blue-toned illustration of a group of livestock: cattle, horse, sheep, pig and chicken"></div>
</section>

<section class="lockup">
  <div class="brand-name">HERD SURE</div>
  <div class="lockup-line">RAPID TEST FOR LIVESTOCK</div>
</section>

</body>
</html>
```